political campaign lawn sign - Governor's Council in Massachuesetts

We are looking for a political lawn sign. We are running a campaign for Governor's Council in Massachusetts. This sign will be on the lawn of homes and businesses so people driving by will see it. It needs to be simple and bold. The last name is long so maybe it could say vote for Carl and then Malbonske will be big a bold on the next line??
We need it to say:
Vote for Carlton Malbonske
Governor's Council.

Target Market(s)

local residents

Industry/Entity Type

Politcal Campaign

Font styles to use
Sans Serif
Other font styles liked:
• not sure what font but a modern looking one such as Helvetica, Arial, Sans Seri, sharp sans..

Colors
0054AA
0677BA
7BADD7
CADEEF
E8F1F8
00AB8E
00BBA5
67D7C9
C6EFE9
E9F9F6
FFF300
FFF600
FEFA6F
FFFEC7
FFFEE8

Requirements
Must have
• My name written out with a Capital D and R but lower case for every other letter so its Carl Malbonske
Nice to have
• modern font , the Colors of the lawn sign should have Blue, Yellow and White something bold that will stand out
Should not have
• any maps of Massachusetts

```html
<!DOCTYPE html>
<html lang="en">
<head>
<meta charset="utf-8">
<title>Vote for Carl Malbonske – Lawn Sign</title>
<link href="https://fonts.googleapis.com/css2?family=Montserrat:wght@400;600;700;800&display=swap" rel="stylesheet">
<style>
  :root {
    --backdrop: #c4c4c4;
    --sign-blue: #0054aa;
    --sign-blue-deep: #003f85;
    --outline-blue: #2f6fbf;
    --accent-yellow: #fff300;
    --name-white: #ffffff;
    --name-light: #7badd7;
    --url-navy: #0d4a9c;
    --url-grey: #3a3f47;
    --panel-white: #ffffff;
  }
  html, body {
    margin: 0;
    padding: 0;
    width: 863px;
    height: 1200px;
    overflow: hidden;
    background: var(--backdrop);
  }
  .canvas {
    position: relative;
    width: 863px;
    height: 1200px;
  }
  .lawn-sign {
    position: absolute;
    left: 42px;
    top: 307px;
    width: 780px;
    height: 585px;
    background: linear-gradient(120deg, var(--sign-blue) 0%, var(--sign-blue) 60%, var(--sign-blue-deep) 100%);
    overflow: hidden;
    box-shadow: 0 28px 40px rgba(0,0,0,0.35);
    font-family: "Montserrat", sans-serif;
  }
  .candidate-portrait {
    position: absolute;
    left: 410px;
    top: 0;
    width: 370px;
    height: 585px;
    background: linear-gradient(180deg, rgba(0,84,170,0) 0%, #2a4a78 55%, #1b2a45 100%);
  }
  .footer-wedge {
    position: absolute;
    left: 0;
    bottom: 0;
    width: 440px;
    height: 115px;
  }
  .headline {
    position: absolute;
    left: 40px;
    top: 30px;
    margin: 0;
    font-weight: 700;
  }
  .echo-line,
  .vote-for {
    display: block;
    font-size: 56px;
    line-height: 47px;
    letter-spacing: 0.5px;
    font-weight: 700;
  }
  .echo-line {
    color: transparent;
    -webkit-text-stroke: 1px var(--outline-blue);
  }
  .vote-for {
    color: var(--accent-yellow);
    margin-top: 2px;
  }
  .first-name {
    display: block;
    font-size: 128px;
    line-height: 108px;
    font-weight: 800;
    color: var(--name-white);
    letter-spacing: -3px;
    margin-top: 4px;
  }
  .last-name {
    display: block;
    font-size: 67px;
    line-height: 64px;
    font-weight: 800;
    color: var(--name-light);
    letter-spacing: -1px;
  }
  .office {
    position: absolute;
    left: 40px;
    top: 408px;
    width: 343px;
    display: flex;
    align-items: center;
    gap: 4px;
    color: var(--name-white);
    font-size: 20px;
    font-weight: 600;
  }
  .office-rule {
    flex: 1;
    height: 1px;
    background: var(--name-white);
    opacity: 0.8;
  }
  .web-address {
    position: absolute;
    left: 41px;
    top: 524px;
    font-size: 25px;
    line-height: 1;
    color: var(--url-grey);
    font-weight: 400;
  }
  .web-address strong {
    color: var(--url-navy);
    font-weight: 700;
  }
</style>
</head>
<body>
<main class="canvas">
  <section class="lawn-sign">
    <div class="candidate-portrait" role="img" aria-label="Portrait photo of the candidate in a dark suit and blue tie"></div>

    <svg class="footer-wedge" viewBox="0 0 440 115" preserveAspectRatio="none" aria-hidden="true">
      <polygon points="0,57 440,0 440,115 0,115" fill="var(--panel-white)"/>
    </svg>

    <h1 class="headline">
      <span class="echo-line" aria-hidden="true">VOTE FOR</span>
      <span class="echo-line" aria-hidden="true">VOTE FOR</span>
      <span class="echo-line" aria-hidden="true">VOTE FOR</span>
      <span class="vote-for">VOTE FOR</span>
      <span class="first-name">Carl</span>
      <span class="last-name">Malbonske</span>
    </h1>

    <p class="office" style="margin:0;">
      <span>Governer's Council</span>
      <span class="office-rule"></span>
    </p>

    <p class="web-address" style="margin:0;"><strong>voteforcarl</strong>.net</p>
  </section>
</main>
</body>
</html>
```